Building company buisness cards

We are looking for a sharp modern new look for our business cards.We are a New Zealand based company that specialises in house and land packages.We have attached a photo of the current logo and would like to see if it can be improved somehow if needed.We are open to any colours but we have chosen Black and White at this stage. Feel free to change the font and make the logo smarter looking.Play with the colours and see what looks best.We want a card that looks so good know one will want to throw it away!

Target Market(s)

Building profesonals, home buyers

Industry/Entity Type

Building

Contact Information for Business Card

Derek Haskins
0274930268
derekh@stonerange.co.nz

Font styles to use
Serif
Sans Serif

Colors

Designer to choose colors to be used in the design.

Requirements
Must have
• Just the logo on one side and details on the other
• Clean simple looking card
Nice to have
• Round corners and detail like raised or spot UV
• Something that stands out
Should not have
• To title needed, Director etc

```html
<!DOCTYPE html>
<html lang="en">
<head>
<meta charset="utf-8">
<title>Stonerange business cards</title>
<link rel="stylesheet" href="https://fonts.googleapis.com/css2?family=Libre+Baskerville:wght@700&family=Arimo:wght@400&display=swap">
<style>
  :root {
    --backdrop: #2a2a2d;
    --card: #1d1e20;
    --card-edge: #2b2c2f;
    --ink-white: #f2f2f2;
    --ink-gloss: #3b3c40;
    --ink-faint: #2c2d30;
    --line: #d9d9d9;
  }
  * { margin: 0; padding: 0; box-sizing: border-box; }
  html, body { width: 1200px; height: 800px; overflow: hidden; }
  body {
    background: var(--backdrop);
    display: flex;
    align-items: center;
    justify-content: center;
    gap: 60px;
    font-family: "Arimo", Arial, sans-serif;
  }
  .card {
    position: relative;
    width: 520px;
    height: 300px;
    background: var(--card);
    border-radius: 18px;
    border: 1px solid var(--card-edge);
    overflow: hidden;
    box-shadow: 0 18px 40px rgba(0,0,0,0.45);
  }
  /* front */
  .card-front .brand {
    position: absolute;
    left: 50%;
    top: 50%;
    transform: translate(-50%, -50%);
    display: flex;
    align-items: center;
    gap: 16px;
  }
  .brand-name {
    font-family: "Libre Baskerville", Georgia, serif;
    font-weight: 700;
    font-size: 44px;
    color: var(--ink-gloss);
    letter-spacing: -0.5px;
  }
  .brand-mark {
    width: 54px; height: 54px;
    border: 3px solid var(--ink-white);
    border-radius: 50%;
  }
  /* back */
  .faint-ring {
    position: absolute;
    right: -70px;
    top: -60px;
    width: 300px; height: 300px;
    border: 10px solid var(--ink-faint);
    border-radius: 50%;
  }
  .back-brand {
    position: absolute;
    left: 40px;
    top: 50%;
    transform: translateY(-50%);
    display: flex;
    flex-direction: column;
    align-items: center;
    gap: 10px;
  }
  .back-brand .brand-mark { width: 70px; height: 70px; }
  .back-brand .brand-name {
    font-size: 16px;
    color: var(--ink-white);
    letter-spacing: 0.5px;
  }
  .divider {
    position: absolute;
    left: 200px;
    top: 90px;
    width: 1.5px;
    height: 120px;
    background: var(--line);
  }
  .details {
    position: absolute;
    left: 232px;
    top: 96px;
    color: var(--ink-white);
  }
  .person-name {
    font-family: "Libre Baskerville", Georgia, serif;
    font-weight: 700;
    font-size: 17px;
    padding-bottom: 8px;
    border-bottom: 1.5px solid var(--line);
    width: 230px;
    margin-bottom: 16px;
  }
  .contact {
    display: flex;
    align-items: center;
    gap: 8px;
    font-size: 14px;
    margin-bottom: 8px;
  }
  .contact svg { width: 16px; height: 16px; flex: none; }
</style>
</head>
<body>
  <section class="card card-front" aria-label="Card front">
    <div class="brand">
      <span class="brand-name">Stonerange</span>
      <span class="brand-mark"></span>
    </div>
  </section>

  <section class="card card-back" aria-label="Card back">
    <div class="faint-ring"></div>
    <div class="back-brand">
      <span class="brand-mark"></span>
      <span class="brand-name">Stonerange</span>
    </div>
    <div class="divider"></div>
    <div class="details">
      <p class="person-name">Derek Haskins</p>
      <p class="contact">
        <svg viewBox="0 0 16 16" aria-hidden="true"><circle cx="8" cy="8" r="7" fill="none" stroke="#f2f2f2" stroke-width="1.2"/><rect x="5.5" y="4" width="5" height="8" rx="1" fill="none" stroke="#f2f2f2" stroke-width="1.1"/></svg>
        <span>0274930268</span>
      </p>
      <p class="contact">
        <svg viewBox="0 0 16 16" aria-hidden="true"><circle cx="8" cy="8" r="7" fill="none" stroke="#f2f2f2" stroke-width="1.2"/><rect x="4" y="5.5" width="8" height="5.5" fill="none" stroke="#f2f2f2" stroke-width="1.1"/><path d="M4 5.5 L8 8.8 L12 5.5" fill="none" stroke="#f2f2f2" stroke-width="1.1"/></svg>
        <span>derekh@stonerange.co.nz</span>
      </p>
    </div>
  </section>
</body>
</html>
```